Automotive component supplier needs a business card design

We need a business card design for our company called Velmar Global Components Ltd based in the UK. We are a supplier of interior and exterior components to premium car manufacturers such as Corvane Hale, Durrant Fyfe, Maxtorn and Valdessimo. We would like to see a modern business card design that uses the colour blue.

Target Market(s)

Premium automotive car manufacturers.

Industry/Entity Type

Automotive

Contact Information for Business Card

Company Name : Velmar Global Components Limited
Address: 17 Tamsey Yard, Upper Drisk, Warwick, CV31 8RJ, United Kingdom
Web Address : www.velmarparts-example.co.uk

Font styles to use
Other font styles liked:
• Helvetica

Colors
3176b5
0255a3
85acd3
cfdeed
cee9f5
85cae6
34a6d7
0692cd
9bcb3c

Requirements
Must have
• Clear company logo and a mixture of blue colours.
Nice to have
• A high quality modern image.
Should not have
• Multiple colours.

```html
<!DOCTYPE html>
<html lang="en">
<head>
<meta charset="utf-8">
<title>Velmar Global Components – Business Card</title>
<link href="https://fonts.googleapis.com/css2?family=Arimo:wght@400;700&display=swap" rel="stylesheet">
<style>
  :root {
    --blue: #0a86c8;
    --blue-deep: #0677b6;
    --blue-light: #1a9ad8;
    --green: #8dc63f;
    --text-grey: #666a6e;
    --rule-grey: #8a8a8a;
    --paper: #ffffff;
    --paper-shade: #e8e8e8;
    --backdrop: #3a3a3a;
  }
  * { margin: 0; padding: 0; box-sizing: border-box; }
  html, body {
    width: 1200px; height: 965px; overflow: hidden;
    background: var(--backdrop);
    font-family: "Arimo", Helvetica, Arial, sans-serif;
  }
  .stage { position: relative; width: 1200px; height: 965px; }
  .card-slot {
    position: absolute; left: 225px; width: 750px; height: 427px; overflow: hidden;
  }
  .card-slot.front-slot { top: 37px; }
  .card-slot.back-slot { top: 500px; }
  .card {
    position: absolute; left: 0; top: 0;
    width: 887px; height: 505px;
    transform: scale(0.8456); transform-origin: 0 0;
  }

  /* Front */
  .card-front {
    background: radial-gradient(ellipse at 60% 30%, var(--paper) 0%, #f6f6f6 50%, var(--paper-shade) 100%);
  }
  .brand { position: absolute; left: 52px; top: 74px; color: var(--blue); font-weight: 700; }
  .brand-name { display: block; font-size: 92px; line-height: 92px; letter-spacing: 2px; }
  .brand-line { display: block; font-size: 25px; letter-spacing: 3.2px; margin-top: 14px; }
  .brand-mark {
    position: absolute; left: 148px; top: 76px; width: 20px; height: 20px;
    background: var(--green);
  }
  .person-name {
    position: absolute; left: 52px; top: 268px;
    font-size: 27px; font-weight: 700; color: var(--blue); letter-spacing: 0.3px;
  }
  .person-role {
    position: absolute; left: 52px; top: 304px;
    font-size: 20px; color: var(--green);
  }
  .role-rule { position: absolute; left: 213px; top: 318px; width: 628px; height: 6px; }
  .contact-list { position: absolute; left: 52px; top: 355px; list-style: none; }
  .contact-list li {
    display: flex; align-items: center; height: 25.5px;
    font-size: 20.5px; color: var(--text-grey);
  }
  .contact-list svg { width: 22px; height: 20px; margin-right: 12px; flex: none; }
  .address {
    position: absolute; right: 46px; top: 380px; text-align: right;
    font-size: 20.5px; line-height: 25.5px; color: var(--text-grey); font-style: normal;
  }
  .footer-band {
    position: absolute; left: 0; bottom: 0; width: 100%; height: 41px; background: var(--blue);
  }
  .footer-band .accent {
    position: absolute; left: 0; top: 0; width: 58px; height: 100%; background: var(--green);
  }

  /* Back */
  .card-back {
    background: radial-gradient(ellipse at 50% 35%, var(--blue-light) 0%, var(--blue) 55%, var(--blue-deep) 100%);
    color: var(--paper);
  }
  .back-brand { position: absolute; left: 0; right: 0; top: 160px; text-align: center; font-weight: 700; }
  .back-brand .brand-name { font-size: 128px; line-height: 128px; letter-spacing: 3px; }
  .back-brand .brand-line { font-size: 32px; letter-spacing: 4.5px; margin-top: 22px; }
  .back-web {
    position: absolute; left: 0; right: 0; top: 462px;
    display: flex; align-items: center; justify-content: center; gap: 20px;
    font-size: 20px; color: var(--paper);
  }
  .back-web .rule { width: 210px; height: 2px; }
  .back-web .rule.left { background: linear-gradient(to right, rgba(255,255,255,0), rgba(210,230,245,0.8)); }
  .back-web .rule.right { background: linear-gradient(to left, rgba(255,255,255,0), rgba(210,230,245,0.8)); }
</style>
</head>
<body>
<main class="stage">

  <div class="card-slot front-slot">
    <section class="card card-front" aria-label="Business card front">
      <div class="brand">
        <span class="brand-name">VELMAR</span>
        <span class="brand-line">GLOBAL COMPONENTS</span>
      </div>

      <h1 class="person-name">DANIEL ASHCROFT</h1>
      <p class="person-role">Founder &amp; CEO</p>
      <svg class="role-rule" viewBox="0 0 628 6" aria-hidden="true">
        <line x1="0" y1="3" x2="148" y2="3" stroke="#0a86c8" stroke-width="2.4" stroke-dasharray="2.4 3.2"/>
        <line x1="92" y1="3" x2="148" y2="3" stroke="#8dc63f" stroke-width="2.4" stroke-dasharray="2.4 3.2"/>
        <line x1="150" y1="3" x2="628" y2="3" stroke="#8a8a8a" stroke-width="2"/>
      </svg>

      <ul class="contact-list">
        <li>
          <svg viewBox="0 0 22 20" aria-hidden="true">
            <rect x="2" y="1" width="5" height="18" rx="1.5" fill="#0a86c8"/>
            <rect x="8" y="3" width="12" height="16" rx="1.5" fill="#0a86c8"/>
            <rect x="10" y="5" width="8" height="3" fill="#fff"/>
            <g fill="#fff"><rect x="10" y="10" width="2" height="2"/><rect x="13" y="10" width="2" height="2"/><rect x="16" y="10" width="2" height="2"/><rect x="10" y="14" width="2" height="2"/><rect x="13" y="14" width="2" height="2"/><rect x="16" y="14" width="2" height="2"/></g>
          </svg>
          + 041 555 01 47
        </li>
        <li>
          <svg viewBox="0 0 22 20" aria-hidden="true">
            <rect x="5" y="0.5" width="11" height="19" rx="2" fill="none" stroke="#0a86c8" stroke-width="1.8"/>
            <rect x="7.5" y="3.5" width="6" height="10" fill="#0a86c8"/>
            <circle cx="10.5" cy="16.5" r="1.2" fill="#0a86c8"/>
          </svg>
          + 0164 555 02 83
        </li>
        <li>
          <svg viewBox="0 0 22 20" aria-hidden="true">
            <rect x="1" y="4" width="20" height="13" fill="#0a86c8"/>
            <polyline points="1,4 11,12 21,4" fill="none" stroke="#fff" stroke-width="1.6"/>
            <line x1="1" y1="17" x2="8" y2="10" stroke="#fff" stroke-width="1.2"/>
            <line x1="21" y1="17" x2="14" y2="10" stroke="#fff" stroke-width="1.2"/>
          </svg>
          info@velmarparts-example.co.uk
        </li>
        <li>
          <svg viewBox="0 0 22 20" aria-hidden="true">
            <g fill="none" stroke="#0a86c8" stroke-width="1.5">
              <circle cx="11" cy="10" r="9"/>
              <ellipse cx="11" cy="10" rx="4" ry="9"/>
              <line x1="2" y1="10" x2="20" y2="10"/>
              <line x1="3.5" y1="5.5" x2="18.5" y2="5.5"/>
              <line x1="3.5" y1="14.5" x2="18.5" y2="14.5"/>
            </g>
          </svg>
          www.velmarparts-example.co.uk
        </li>
      </ul>

      <address class="address">
        17 Tamsey Yard, Upper Drisk,<br>
        Warwick, CV31 8RJ<br>
        United Kingdom
      </address>

      <div class="footer-band"><span class="accent"></span></div>
    </section>
  </div>

  <div class="card-slot back-slot">
    <section class="card card-back" aria-label="Business card back">
      <div class="back-brand">
        <span class="brand-name">VELMAR</span>
        <span class="brand-line">GLOBAL COMPONENTS</span>
      </div>
      <div class="back-web">
        <span class="rule left"></span>
        <span>www.velmarparts-example.co.uk</span>
        <span class="rule right"></span>
      </div>
    </section>
  </div>

</main>
</body>
</html>
```